METAL FABRICATION BUSINESS CARD

** I will be ending the project and picking design early. This Friday October 3rd at 7am MST if not sooner**
ONE SIDED BUSINESS CARD ONLY. AND LOGO SIZE TO BE DOMINANT so it stands out.
Looking for a black background and will be doing raised chrome/silver font on the business cards. Looking to have the following on the front of the business card. Company logo is uploaded in files.
Company logo
*Compartment Doors
*Roof Radius Metal
*J-Wrap Metal Skirting
*S-Lock Beltline Molding
*Pre-Bent Molding
and more...
Owen Daltry 307.552.4198 info@KX-Welt.com
Updates
One sided business card only please. Also logo size should be dominant and sized bigger
Contact Information for Business Card
Black background, Text will be raised chrome/silver, and corners will be rounded.

```html
<!DOCTYPE html>
<html lang="en">
<head>
<meta charset="utf-8">
<title>KX-Welt Business Card</title>
<link rel="stylesheet" href="https://fonts.googleapis.com/css2?family=Open+Sans:wght@400;600;700&display=swap">
<style>
  :root {
    --backdrop: #1b1b1b;
    --card: #000000;
    --chrome: #c9c9c9;
    --chrome-bright: #e6e6e6;
    --chrome-dim: #8e8e8e;
    --rule: #9a9a9a;
  }
  html, body {
    margin: 0;
    padding: 0;
    width: 1200px;
    height: 1059px;
    overflow: hidden;
    background: var(--backdrop);
    font-family: "Open Sans", sans-serif;
  }
  .card {
    position: absolute;
    left: 187px;
    top: 294px;
    width: 840px;
    height: 478px;
    background: var(--card);
    border-radius: 26px;
    box-shadow: 0 8px 24px rgba(0,0,0,0.6);
  }
  .brand {
    position: absolute;
    left: 0;
    right: 0;
    top: 60px;
    text-align: center;
    font-size: 66px;
    font-weight: 700;
    color: var(--chrome);
    letter-spacing: 1px;
    margin: 0;
  }
  .person-name {
    position: absolute;
    left: 44px;
    top: 216px;
    margin: 0;
    font-size: 30px;
    font-weight: 600;
    color: var(--chrome);
  }
  .divider {
    position: absolute;
    left: 42px;
    width: 756px;
    top: 276px;
    height: 2px;
    background: linear-gradient(90deg, #555, var(--chrome-bright) 50%, #555);
  }
  .contact {
    position: absolute;
    top: 300px;
    display: flex;
    align-items: center;
    gap: 12px;
    font-size: 21px;
    color: var(--chrome);
  }
  .contact-phone { left: 45px; }
  .contact-email { right: 40px; }
  .contact svg { fill: var(--chrome-bright); }
  .services {
    position: absolute;
    left: 0;
    right: 0;
    top: 352px;
    margin: 0;
    padding: 0;
    list-style: none;
    text-align: center;
    font-size: 20px;
    font-weight: 600;
    line-height: 35px;
    color: var(--chrome);
  }
  .services .dim { color: var(--chrome-dim); }
</style>
</head>
<body>
  <div class="card">
    <h1 class="brand">KX-Welt</h1>
    <h2 class="person-name">Owen Daltry</h2>
    <div class="divider"></div>
    <div class="contact contact-phone">
      <svg width="22" height="22" viewBox="0 0 24 24" aria-hidden="true">
        <path d="M6.6 10.8c1.4 2.8 3.8 5.1 6.6 6.6l2.2-2.2c.3-.3.7-.4 1-.2 1.1.4 2.3.6 3.6.6.6 0 1 .4 1 1V20c0 .6-.4 1-1 1C10.6 21 3 13.4 3 4c0-.6.4-1 1-1h3.5c.6 0 1 .4 1 1 0 1.3.2 2.5.6 3.6.1.3 0 .7-.2 1z"/>
      </svg>
      <span>307.552.4198</span>
    </div>
    <div class="contact contact-email">
      <svg width="22" height="16" viewBox="0 0 22 16" aria-hidden="true">
        <path d="M0 0h22v16H0z M2 2v1l9 6 9-6V2z" fill-rule="evenodd"/>
      </svg>
      <span>info@KX-Welt.com</span>
    </div>
    <ul class="services">
      <li><span class="dim">• Compartment Doors</span> • Roof Radius Metal</li>
      <li>• J-Wrap Metal Skirting • S-Lock Beltline Molding</li>
      <li>• Pre-Bent Molding&nbsp; and more...</li>
    </ul>
  </div>
</body>
</html>
```